Brightwave Travel and Tours

Hotel Reservations
Airline Ticketing
Day Tour

My business is a Travel agency. My services are issuing domestic and international tickets. Book room/hotel reservations local/international.
My color preference is apple green/orange/red/blue.
Images of beaches, tickets,luggage.

Industry/Entity Type

Business

```html
<!DOCTYPE html>
<html lang="en">
<head>
<meta charset="utf-8">
<title>Brightwave Travel and Tours – Business Card</title>
<link rel="stylesheet" href="https://fonts.googleapis.com/css2?family=Open+Sans:wght@400;600&display=swap">
<style>
  :root {
    --backdrop: #2b2623;
    --card: #151515;
    --card-edge: #222222;
    --brand-blue: #1f86b5;
    --tagline-cyan: #62c9ea;
    --info-white: #e6eef2;
    --divider: #4a4a4a;
  }
  html, body {
    margin: 0;
    width: 1200px;
    height: 780px;
    overflow: hidden;
    background: var(--backdrop);
    font-family: "Open Sans", Arial, sans-serif;
  }
  .canvas {
    position: relative;
    width: 1200px;
    height: 780px;
  }
  .card {
    position: absolute;
    top: 238px;
    width: 530px;
    height: 303px;
    background: var(--card);
    border: 1px solid var(--card-edge);
    box-sizing: border-box;
    border-radius: 3px;
  }
  .card--front { left: 50px; }
  .card--back { left: 620px; }

  .brand {
    display: flex;
    align-items: center;
    gap: 10px;
    color: var(--brand-blue);
    font-weight: 600;
    font-size: 19px;
    line-height: 1.2;
  }
  .brand__dot {
    flex: none;
    width: 22px;
    height: 22px;
    border-radius: 50%;
    background: var(--brand-blue);
  }

  .card--front .brand {
    position: absolute;
    top: 112px;
    left: 0;
    right: 0;
    justify-content: center;
  }
  .tagline {
    position: absolute;
    top: 178px;
    left: 0;
    right: 0;
    text-align: center;
    color: var(--tagline-cyan);
    font-size: 15px;
    letter-spacing: 0.2px;
    margin: 0;
  }

  .card--back .brand {
    position: absolute;
    top: 110px;
    left: 26px;
    width: 210px;
    font-size: 18px;
  }
  .card--back .divider {
    position: absolute;
    left: 250px;
    top: 52px;
    width: 1px;
    height: 200px;
    background: var(--divider);
  }
  .contact {
    position: absolute;
    left: 272px;
    top: 62px;
    right: 18px;
    color: var(--info-white);
    font-size: 14px;
    line-height: 1.35;
  }
  .contact__name {
    margin: 0;
    color: var(--brand-blue);
    font-size: 22px;
    font-weight: 600;
    line-height: 1.1;
  }
  .contact__role {
    margin: 0 0 12px;
    font-size: 15px;
  }
  .contact__line {
    margin: 0;
    display: flex;
    align-items: center;
    gap: 7px;
  }
  .contact__icon {
    flex: none;
    width: 14px;
    height: 14px;
  }
  .contact__web {
    margin: 8px 0 0;
    color: var(--brand-blue);
  }
</style>
</head>
<body>
<main class="canvas">

  <section class="card card--front" aria-label="Card front">
    <div class="brand">
      <span class="brand__dot"></span>
      <span class="brand__name">Brightwave Travel and Tours</span>
    </div>
    <p class="tagline">Hotel Reservations | Airline Ticketing | Day Tour</p>
  </section>

  <section class="card card--back" aria-label="Card back">
    <div class="brand">
      <span class="brand__dot"></span>
      <span class="brand__name">Brightwave Travel and Tours</span>
    </div>
    <div class="divider"></div>
    <div class="contact">
      <p class="contact__name">Employee Name</p>
      <p class="contact__role">Managing Director</p>
      <p class="contact__line">your address Rd., Suite 000</p>
      <p class="contact__line">Harbor City, USA</p>
      <p class="contact__line">
        <svg class="contact__icon" viewBox="0 0 14 14" aria-hidden="true">
          <rect width="14" height="14" rx="2" fill="#e6eef2"/>
          <path d="M4 3 L6 3 L6.6 5.4 L5.4 6.2 Q6.4 8 7.8 8.6 L8.6 7.4 L11 8 L11 10 Q7 11 4.5 7.5 Q3 5.4 4 3 Z" fill="#151515"/>
        </svg>
        000.000.0000
      </p>
      <p class="contact__line">
        <svg class="contact__icon" viewBox="0 0 14 14" aria-hidden="true">
          <rect width="14" height="14" rx="2" fill="#e6eef2"/>
          <rect x="2.5" y="4" width="9" height="6.5" fill="none" stroke="#151515" stroke-width="1.2"/>
          <path d="M2.5 4 L7 7.8 L11.5 4" fill="none" stroke="#151515" stroke-width="1.2"/>
        </svg>
        info@youremail.com
      </p>
      <p class="contact__web">www.yourwebsite.com</p>
    </div>
  </section>

</main>
</body>
</html>
```